Takeout Menu Design for Japanese Restaurant.

I need to have a takeout menu designed for my newly opened restaurant. I uploaded a word file with very specific information on the project overall. Please download it to understand the scope.
Updates

Hello designers,

I have posted an archive containing some updated files. I will provide the explanation for each piece below:

1. The PDF and the 2.jpg represent the photos that are supposed to appear on the Teppanyaki panel. I do not know how to extract the photo from the PDF so I uploaded it as is. There is no higher resolution version of 2.jpg. If useable, choose one that is more appropriate for the menu, if not, use a stock photo with similar configuration as presented in the photos.

2. The screenshot is a mock up of how I want the map to represent. The town is large so clearly marking the Brell-Mart is a priority. Obviously, I want the final map to look much better than the screenshot I uploaded. You can simply grap the Pindo Charts file I uploaded in the previous archive and clean it up of irrelevant information such as other businesses, buildings and texts and colour in where the Brell-Mart is supposed to be blue and preferably use the Brellmart symbol. Also, please make where the restaurant is more apparent, not just a location marker A. 

3. The Teppanyaki Directive.docx contains text that is supposed to appear on the Teppanyaki panel, superimposing the photo, which is supposed to cover most, if not all of the panel. I think it is pretty clear, if not, please specify which areas you need explained. 

Industry/Entity Type

Restaurant

Requirements
Must have
• - Restaurant name & logo.
- On the front stating a new restaurant or grand opening (Must be apparent.)
- Hours of operation.
- Contact information (phone number and fax.)
- Website address.
- Stylized map showing approximate address of establishment.
- Specific address of establishment
- Menu items.

- The flyer is 11 X 17. The design templates for specific measurements are provided.
- Double sided (6 panels in all. Roll fold.)

```html
<!DOCTYPE html>
<html lang="en">
<head>
<meta charset="utf-8">
<title>Kaito Takeout Menu</title>
<link href="https://fonts.googleapis.com/css2?family=Arimo:wght@400;700&display=swap" rel="stylesheet">
<style>
:root{
  --frame:#1d1d1d;
  --red-dark:#5e0f14;
  --red-mid:#8c1a20;
  --red-bright:#b02a30;
  --menu-red:#a01e22;
  --grey-band:#5b5b5b;
  --paper:#ffffff;
  --ink:#222222;
  --gold:#c7a064;
  --cream:#f1f1ec;
}
*{margin:0;padding:0;box-sizing:border-box}
html,body{width:1200px;height:792px;overflow:hidden;background:var(--frame)}
body{font-family:"Arimo",Arial,sans-serif;color:var(--ink)}
.brochure{position:relative;width:1200px;height:792px;background:var(--frame)}

/* left menu panel */
.menu-panel{position:absolute;left:9px;top:9px;width:397px;height:774px;background:var(--paper)}
.menu-header{height:73px;background:var(--grey-band);color:#fff;text-align:center;padding-top:10px}
.menu-header h2{font-size:14px;font-weight:700}
.menu-header p{font-size:9px;line-height:11px;width:270px;margin:2px auto 0}
.menu-col{position:absolute;top:85px;width:178px}
.menu-col.first{left:22px}
.menu-col.second{left:212px;top:82px}
.menu-section{margin-bottom:14px}
.menu-section h3{color:var(--menu-red);font-size:9px;font-weight:700;margin-bottom:9px}
.item{margin-bottom:6px;font-size:5.6px;line-height:6.6px}
.item b{display:block;font-weight:700}

/* centre panel */
.centre-panel{position:absolute;left:406px;top:9px;width:388px;height:774px;
  background:linear-gradient(180deg,var(--red-mid),var(--red-dark))}
.kitchen-photo{position:absolute;left:0;top:73px;width:388px;height:284px;
  background:radial-gradient(circle at 55% 55%,#e0862e 0,#6b3a22 25%,#2a2220 65%,#151212 100%)}
.teppanyaki-block{position:absolute;left:0;top:357px;width:388px;height:235px;background:var(--paper);text-align:center}
.teppanyaki-block h3{color:var(--menu-red);font-size:11px;font-weight:700;margin-top:62px}
.teppanyaki-block p{font-size:10px;line-height:13px;margin:12px auto 0;width:340px}
.map-area{position:absolute;left:36px;top:608px;width:316px;height:165px;background:var(--cream);border:3px solid #d8d2c2}
.map-fill{width:100%;height:100%;background:linear-gradient(135deg,#e8e9e2,#d7dccf 60%,#c9d6e0)}

/* right cover panel */
.cover-panel{position:absolute;left:794px;top:9px;width:397px;height:774px;
  background:radial-gradient(ellipse at 55% 30%,var(--red-bright),var(--red-mid) 50%,var(--red-dark))}
.hero-frame{position:absolute;left:20px;top:25px;width:344px;height:357px;background:var(--gold);padding:9px}
.hero-photo{width:100%;height:100%;background:radial-gradient(circle at 70% 55%,#6d7a3a 0,#3a2a1e 40%,#0d0d0d 80%)}
.opening-ribbon{position:absolute;left:20px;top:25px;width:200px;height:200px;overflow:hidden}
.opening-ribbon svg{display:block}
.brand{position:absolute;left:0;width:397px;text-align:center}
.brand-name{top:470px;font-size:78px;font-weight:700;color:#fff;letter-spacing:4px}
.brand-tag{top:560px;font-size:11.5px;color:var(--gold);letter-spacing:2px}
.contact{position:absolute;left:0;top:605px;width:397px;text-align:center;color:#fff;font-size:11px;line-height:15px}
.contact .strong{font-weight:700;font-size:11.5px}
.contact .web{font-weight:700;margin-top:14px}
.contact .hours-title{font-weight:700;margin-top:14px}
</style>
</head>
<body>
<div class="brochure">

  <section class="menu-panel">
    <header class="menu-header">
      <h2>Maki</h2>
      <p>A variety of sushi where ingredients are rolled into a cylinder and then cut into bite sized pieces.</p>
    </header>

    <div class="menu-col first">
      <div class="menu-section">
        <h3>Classic Maki</h3>
        <div class="item"><b>Cream City (G1) - $10.95</b>Smoked salmon, scallion, cucumber and cream cheese.</div>
        <div class="item"><b>California (G2) - $6.95</b>Crab, avocado and mayonnaise.</div>
        <div class="item"><b>BC (G3) - $6.95</b>BBQ salmon skin, cucumber and teriyaki sauce.</div>
        <div class="item"><b>Alaska (G4) - $8.95</b>Crab, smoked salmon, avocado and mayonnaise.</div>
        <div class="item"><b>Dynamite (G5) - $8.95</b>Prawn tempura, cucumber, avocado and eel sauce.</div>
        <div class="item"><b>Chopped Scallop (G6) - $7.95</b>Scallop, smelt roe, avocado and mayonnaise.</div>
        <div class="item"><b>Salmon (G7) - $5.95</b></div>
        <div class="item"><b>Tuna (G8) - $5.95</b></div>
        <div class="item"><b>Negi Toro (G9) - $7.95</b>Fatty tuna belly and scallion.</div>
        <div class="item"><b>Tuna Crunch (G10) - $7.95</b>Tuna, tempura flakes and mayonnaise.</div>
        <div class="item"><b>Unagi (G11) - $8.95</b>BBQ eel, cucumber and eel sauce.</div>
        <div class="item"><b>Chicken Teriyaki (G12) - $6.95</b>Grilled chicken, cucumber, lettuce and teriyaki sauce.</div>
        <div class="item"><b>Spider (G13) - $8.95</b>Lightly battered soft shell crab, fish roe, avocado, cucumber, lettuce and eel sauce.</div>
      </div>
      <div class="menu-section">
        <h3>Fruity Maki</h3>
        <div class="item"><b>California Mango (G14) - $6.95</b>Crab, mango, cucumber, and mayonnaise.</div>
        <div class="item"><b>Mango Tuna (G15) - $6.95</b>Tuna, mango, and avocado.</div>
        <div class="item"><b>Electric Banana (G16) - $12.95</b>BBQ eel, avocado, banana tempura, and eel sauce.</div>
        <div class="item"><b>Fancy (G17) - $11.95</b>Prawn tempura, mango, avocado, and cream cheese. Wrapped in soybean sheet.</div>
        <div class="item"><b>Reggae Roll (G18) - $11.95</b>Tuna, mango, avocado and wasabi mayonnaise.</div>
        <div class="item"><b>Greenie (G19) - $12.95</b>Prawn tempura and mango. Wrapped in avocado.</div>
      </div>
      <div class="menu-section">
        <h3>Kaito Desire Maki</h3>
        <div class="item"><b>Orange Crush (G20) - $12.95</b>Crab, salmon, asparagus, avocado, cream cheese and spicy mayonnaise.</div>
        <div class="item"><b>Happy Eel (G21) - $13.95</b>BBQ eel, crab, masago, scallion and cream cheese. Lightly battered and deep-fried. Decorated with spicy mayonnaise and eel sauce.</div>
        <div class="item"><b>Volcano (G22) - $13.95</b>Tuna, scallop and avocado. Deep fried and served on a bed of</div>
      </div>
    </div>

    <div class="menu-col second">
      <div class="menu-section">
        <div class="item"><b>Spicy Salmon (G27) - $6.95</b>Salmon, cucumber and spicy sauce.</div>
        <div class="item"><b>Spicy Tuna (G28) - $6.95</b>Tuna, cucumber and spicy sauce.</div>
        <div class="item"><b>Spicy Salmon Crunch (G29) - $8.95</b>Salmon, tempura flakes and spicy sauce.</div>
        <div class="item"><b>Red Ninja (G30) - $12.95</b>Spicy tuna and tempura flakes. Topped with tempura salmon and tempura avocado. Decorated with masago and mayonnaise.</div>
        <div class="item"><b>White Ninja (G31) - $12.95</b>Spicy tuna and tempura flakes. Topped with avocado. Decorated with eel sauce and mayonnaise.</div>
        <div class="item"><b>Tiger's Eye (G32) - $12.95</b>Salmon, jalapeno and cream cheese. Lightly battered tempura style and topped with wasabi mayonnaise.</div>
        <div class="item"><b>Las Vegas (G33) - $13.95</b>BBQ eel, crab, avocado and cream cheese. Tempura style and served spicy mayonnaise.</div>
      </div>
      <div class="menu-section">
        <h3>Creative Maki</h3>
        <div class="item"><b>Found Coral (G34) - $13.95</b>Soft shell crab tempura, asparagus and avocado topped with seared salmon and unagi sauce.</div>
        <div class="item"><b>Crunchy (G35) - $13.95</b>Smoked salmon, crab and cucumber topped with smelt fish roe and tempura flakes.</div>
        <div class="item"><b>Dragon (G36) - $14.95</b>Prawn tempura, avocado and cucumber wrapped over BBQ eel tempura. Decorated with eel sauce and mayonnaise.</div>
        <div class="item"><b>Skipper Crunch (G37) - $10.95</b>Deep-fried breaded California rolls decorated with eel sauce and mayonnaise.</div>
        <div class="item"><b>Tuna Tataki Roll (G38) - $12.95</b>California rolls topped with seared tuna and unagi sauce.</div>
        <div class="item"><b>Rainbow (G39) - $13.95</b>Crab and cucumber wrapped over salmon, tuna and avocado.</div>
        <div class="item"><b>Little Piglet (G40) - $12.95</b>Crispy bacon, scallop, and asparagus topped with fish roe and unagi sauce.</div>
        <div class="item"><b>Japanese Cowboy (G41) - $10.95</b>Beef teriyaki, asparagus and lettuce with a touch of teriyaki sauce.</div>
      </div>
      <div class="menu-section">
        <h3>Vegetable Maki</h3>
        <div class="item"><b>Sunshine (G42) - $8.95</b>Mango, avocado and cream cheese. Wrapped in soybean sheets.</div>
        <div class="item"><b>Buddha (G43) - $7.95</b>Yam tempura, asparagus, avocado and lettuce.</div>
        <div class="item"><b>Mango Paradise (G44) - $7.95</b>Mango, avocado, inari and cucumber.</div>
        <div class="item"><b>Banana (G45) - $8.95</b>Banana tempura, avocado and cream cheese. Topped with miso sauce.</div>
        <div class="item"><b>Vegetable (G46) - $7.95</b>Avocado, cucumber, carrot, asparagus, red pepper and lettuce.</div>
        <div class="item"><b>Avocado (G47) - $5.95</b>Avocado.</div>
        <div class="item"><b>Yam (G48) - $5.95</b>Yam.</div>
        <div class="item"><b>Kappa (G49) - $4.95</b>Cucumber.</div>
      </div>
    </div>
  </section>

  <section class="centre-panel">
    <div class="kitchen-photo" role="img" aria-label="Photo of chefs cooking with flames on a teppanyaki grill before seated guests"></div>
    <div class="teppanyaki-block">
      <h3>Teppanyaki</h3>
      <p>Teppanyaki is a style of Japanese cuisine that uses an iron griddle to cook food. It is as much a performance art as it is delicious. This unique experience is one of a kind in Ridgemont.<br>For more information and Teppanyaki menu, please visit our website.</p>
    </div>
    <div class="map-area">
      <div class="map-fill" role="img" aria-label="Street map marking the restaurant location beside Brellmart"></div>
    </div>
  </section>

  <section class="cover-panel">
    <div class="hero-frame">
      <div class="hero-photo" role="img" aria-label="Photo of sushi rolls garnished with lemon slices on a dark reflective surface"></div>
    </div>
    <div class="opening-ribbon">
      <svg width="200" height="200" viewBox="0 0 200 200" aria-hidden="true">
        <polygon points="0,115 115,0 175,0 0,175" fill="#c0262c"/>
        <polygon points="0,115 115,0 122,0 0,122" fill="#e04a4f"/>
        <text x="78" y="92" transform="rotate(-45 78 92)" text-anchor="middle" fill="#fff" font-family="Arimo, Arial, sans-serif" font-weight="700" font-size="19">GRAND</text>
        <text x="96" y="110" transform="rotate(-45 96 110)" text-anchor="middle" fill="#fff" font-family="Arimo, Arial, sans-serif" font-weight="700" font-size="19">OPENING</text>
      </svg>
    </div>
    <div class="brand brand-name">KAITO</div>
    <div class="brand brand-tag">TEPPANYAKI - JAPANESE - FUSION</div>
    <div class="contact">
      <div class="strong">Phone: (555) 014-2230</div>
      <div class="strong">Fax: (555) 014-2231</div>
      <div>4820 Alder St. Suite #106 (Besides Brellmart). Ridgemont</div>
      <div class="web">www.kaitoridgemont.com</div>
      <div class="hours-title">Hours of Operation</div>
      <div>Sunday to Thursday: 11:00AM – 10:00PM</div>
      <div>Friday and Saturday: 11:00AM – 11:00PM</div>
    </div>
  </section>

</div>
</body>
</html>
```